依頼詳細
春に向けて、プリスクールの生徒募集を行う方法として、チラシをポスティングする計画をしてます。そのために必要なチラシの作成を依頼したいです。対象年齢が2歳から6歳(小学校就学前まで)の子供を持つ親に対してアピールをしていきますので、英語と子供について関心を寄せそうな見た目を希望致します。今回の募集に合わせ、入会金21600円を無料で行います。また、随時無料体験レッスンを行っていきます。
記載項目
ロデリアイングリッシュスクール/0120−5718(ロデリア)−42(ハロー)/月2回10、800円(税込)から/プリスクールなら英会話のロデリア/ロゴ添付
サイズ
B4
ページ数
片面
希望イメージ
シンプル 複雑
単色 カラフル
暗い 明るい
日常 高級
遊び心 厳粛
未来的 伝統的
女性的 男性的
希望する色
納品ファイル
• 高解像度JPG (.jpg)
• イラストレーター形式 (.ai)
• フォトショップ形式 (.psd)
補足説明

ポスティング用のチラシであるため、見た目ですぐ募集の内容が分かることを第1のポイントとしました。第2のポイントは、弊社より提示した情報以外の情報が入っているか。第3のポイントは、チラシがB4であるため、半分に折られる想定がなされているかでした。

ご提案ありがとうございます。
初めて利用しましたが、ワクター皆様のスキルの高さに驚きました。
また、利用させていただきますのでよろしくお願いします。

```html
<!DOCTYPE html>
<html lang="ja">
<head>
<meta charset="utf-8">
<title>ロデリアイングリッシュスクール 生徒募集</title>
<link rel="stylesheet" href="https://fonts.googleapis.com/css2?family=M+PLUS+Rounded+1c:wght@500;700;800;900&family=Kosugi+Maru&display=swap">
<style>
:root{
  --sky:#dff3fb;
  --blue:#1b8fd8;
  --navy:#1d4f8c;
  --orange:#f28a1e;
  --yellow:#ffd23f;
  --pink:#e9507f;
  --green:#3aae4a;
  --ink:#333;
  --white:#fff;
  --line:#9fcbe2;
}
*{margin:0;padding:0;box-sizing:border-box}
html,body{width:849px;height:1200px;overflow:hidden;background:var(--white)}
.flyer{position:relative;width:849px;height:1200px;overflow:hidden;
  background:linear-gradient(180deg,var(--sky) 0%,#eaf7fc 60%,var(--sky) 100%);
  font-family:"M PLUS Rounded 1c","Kosugi Maru",sans-serif;color:var(--ink)}
.abs{position:absolute}
.lead-left{left:22px;top:22px;transform:rotate(-10deg);color:var(--navy);font-weight:900;font-size:30px;line-height:1.15;text-align:center}
.lead-right{right:22px;top:34px;transform:rotate(9deg);color:var(--green);font-weight:900;font-size:24px;line-height:1.2;text-align:center}
.title-main{left:0;right:0;top:26px;text-align:center;font-weight:900;font-size:112px;line-height:1;letter-spacing:4px;
  -webkit-text-stroke:4px var(--navy);paint-order:stroke fill}
.title-main .c1{color:var(--orange)}.title-main .c2{color:var(--yellow)}.title-main .c3{color:var(--pink)}
.title-sub{left:0;right:0;top:140px;text-align:center;font-weight:900;font-size:118px;line-height:1;color:var(--blue);
  -webkit-text-stroke:6px var(--white);paint-order:stroke fill;letter-spacing:2px;white-space:nowrap}
.photo-girl{left:-20px;top:250px;width:470px;height:400px;border-radius:0 50% 50% 0/0 50% 50% 0;
  background:radial-gradient(circle at 45% 45%,#f6d6c2 0%,#e9b89a 35%,#c89070 60%,#a9d8ee 100%)}
.recruit{left:470px;top:322px;width:345px;height:84px;border-radius:42px;background:var(--pink);color:var(--white);
  font-weight:900;font-size:60px;letter-spacing:10px;text-align:center;line-height:84px;box-shadow:0 4px 0 #b83561}
.info{left:455px;top:428px;width:370px;border-collapse:collapse;background:var(--white);font-size:14px}
.info th{width:92px;background:#eef8fd;color:var(--navy);font-weight:800;border:1px solid var(--line);padding:10px 4px;text-align:center}
.info td{border:1px solid var(--line);padding:10px 12px;line-height:1.55;font-weight:500}
.offer{left:24px;top:640px;width:320px;height:320px;border-radius:50%;background:var(--white);border:6px solid var(--blue);text-align:center;padding-top:30px}
.offer-now{color:var(--pink);font-weight:900;font-size:44px;line-height:1}
.offer-fee{color:var(--navy);font-weight:900;font-size:30px;line-height:1.2;margin-top:12px}
.offer-free{color:var(--orange);font-weight:900;font-size:86px;line-height:1;-webkit-text-stroke:3px var(--navy);paint-order:stroke fill}
.offer-end{color:var(--navy);font-weight:900;font-size:32px;line-height:1.2}
.bubble{left:318px;top:772px;width:112px;height:78px;border-radius:50%;background:var(--white);border:2px solid var(--navy);
  color:var(--navy);font-weight:800;font-size:13px;line-height:1.25;text-align:center;padding-top:14px}
.family{left:340px;top:840px;width:270px;height:180px;border-radius:45% 45% 10px 10px;
  background:linear-gradient(180deg,#f7c9a5 0%,#7fb6e0 55%,#f39a55 100%)}
.cozy{left:612px;top:836px;transform:rotate(-12deg);color:var(--orange);font-weight:900;font-size:30px;line-height:1.2;text-align:center;
  -webkit-text-stroke:5px var(--white);paint-order:stroke fill}
.photo-boy{left:700px;top:930px;width:149px;height:120px;border-radius:40px 0 0 40px;
  background:linear-gradient(135deg,#f3c7a8 0%,#6ea8d8 100%)}
.footer{left:0;top:1060px;width:849px;height:140px;background:var(--white);border-top:5px solid var(--blue)}
.trial{left:714px;top:968px;width:130px;height:130px}
.trial-text{left:714px;top:996px;width:130px;text-align:center;color:var(--pink);font-weight:900;font-size:14px;line-height:1.25}
.mascots{left:20px;top:1072px;width:180px;height:118px;border-radius:24px;background:linear-gradient(90deg,#f5c9d6,#b9d8f0)}
.footer-copy{left:210px;top:1074px;width:490px;text-align:center;color:var(--blue);font-size:15px;font-weight:700;white-space:nowrap}
.school-name{left:200px;top:1096px;width:510px;text-align:center;color:var(--navy);font-weight:900;font-size:28px;line-height:1.3;
  display:flex;align-items:center;justify-content:center;gap:10px;white-space:nowrap}
.school-name .mark{flex:0 0 16px;width:16px;height:16px;border-radius:50%;background:var(--orange)}
.phone{left:200px;top:1140px;width:510px;display:flex;align-items:center;justify-content:center;gap:10px;color:var(--orange);font-weight:900;font-size:40px;line-height:1;white-space:nowrap}
.phone svg{flex:0 0 40px}
</style>
</head>
<body>
<main class="flyer">
  <p class="abs lead-left">日本人と<br>外国人<br>教師の</p>
  <p class="abs lead-right">外国人<br>教師は100%<br>ネイティブ講師!</p>
  <h1 class="abs title-main"><span class="c1">英</span><span class="c2">会</span><span class="c3">話</span></h1>
  <p class="abs title-sub">プリスクール</p>

  <div class="abs photo-girl" role="img" aria-label="笑顔の女の子の写真"></div>

  <p class="abs recruit">生徒募集</p>

  <table class="abs info">
    <tr><th>対象年齢</th><td>2歳から小学校就学前まで</td></tr>
    <tr><th>開催曜日</th><td>土曜日(月2回)10,800円(税込)から</td></tr>
    <tr><th>時　間</th><td>午前10時から14時までの<br>4時間預かり</td></tr>
    <tr><th>内　容</th><td>日本人講師、外国人講師で4時間の預かりの中で、英語の環境で、英語レッスン、ランチ、オリジナルクラフト作成、月のイベント、教材などを行いながら過ごします。また、日常生活に欠かせない着替えやトイレトレーニングなど、日常的なサポートも行います。</td></tr>
  </table>

  <div class="abs offer">
    <p class="offer-now">今なら!</p>
    <p class="offer-fee">入会金<br>21,600円が</p>
    <p class="offer-free">無料!</p>
    <p class="offer-end">です!</p>
  </div>

  <p class="abs bubble">Let's<br>learn English<br>together</p>
  <div class="abs family" role="img" aria-label="手をつなぐ家族のイラスト"></div>
  <p class="abs cozy">少人数の<br>アットホームな<br>教室です!</p>

  <div class="abs photo-boy" role="img" aria-label="手を挙げる男の子の写真"></div>

  <footer class="abs footer"></footer>

  <svg class="abs trial" viewBox="0 0 100 100" aria-hidden="true">
    <polygon fill="#ffd23f" points="50,2 59,20 78,10 76,31 97,32 84,48 97,66 76,68 78,89 59,80 50,98 41,80 22,89 24,68 3,66 16,48 3,32 24,31 22,10 41,20"/>
  </svg>
  <p class="abs trial-text">随時<br>無料体験<br>レッスン<br>開催中!</p>

  <div class="abs mascots" role="img" aria-label="スクールのマスコットキャラクターのイラスト"></div>
  <p class="abs footer-copy">プリスクールなら英会話のロデリア</p>
  <p class="abs school-name"><span class="mark"></span><span>ロデリアイングリッシュスクール</span></p>
  <p class="abs phone">
    <svg width="40" height="40" viewBox="0 0 24 24" aria-hidden="true"><circle cx="12" cy="12" r="12" fill="#f28a1e"/><path fill="#fff" d="M8.2 5.5l2 2.6c.3.4.3 1-.1 1.4l-1 1c.8 1.6 2 2.8 3.6 3.6l1-1c.4-.4 1-.4 1.4-.1l2.6 2c.4.3.5.9.2 1.3l-1 1.3c-.5.6-1.3.9-2.1.6-3.6-1.2-6.4-4-7.6-7.6-.3-.8 0-1.6.6-2.1l1.3-1c.4-.3 1-.2 1.1 0z"/></svg>
    <span>0120-5718-42</span>
  </p>
</main>
</body>
</html>
```